Banner Ad to promote Youth Cycling Camps

We need a 728 x 90 banner ad to promote some youth cycling camps. There are 2 different camps - a road camp where they learn to ride their bikes on the roads and a mountain bike camp. The camps teach bike handling skills and racing tactics.

Target Market(s)

Parents of youth ages 7-17

Industry/Entity Type

Non-Profit

Font styles to use
Sans Serif

Requirements
Must have
• Logo
• Dates - Road Camp May 5-7, 2017
• - Mountain Bike Camp July 14-16, 2017
• website - quadrapedalcup.org
• be 728 x 90
Nice to have
• Animated - would like it to rotate with 3 slides - 1 a focus on both camps, 1 on road camp, 1 on mountain bike camp

```html
<!DOCTYPE html>
<html lang="en">
<head>
<meta charset="utf-8">
<title>Quadrapedal Cup – Youth Cycling Camps Banners</title>
<link rel="stylesheet" href="https://fonts.googleapis.com/css2?family=Bebas+Neue&family=Kaushan+Script&family=Montserrat:wght@500;800&display=swap">
<style>
  :root {
    --stage: #e9f4fa;
    --banner: #74c6ee;
    --banner-deep: #5fb6e2;
    --ink: #15263a;
    --white: #ffffff;
    --photo-road-a: #8fa3b3;
    --photo-road-b: #4d5a66;
    --photo-forest-a: #3e5a44;
    --photo-forest-b: #9fb0b8;
  }
  * { box-sizing: border-box; margin: 0; padding: 0; }
  html, body { width: 1200px; height: 600px; overflow: hidden; }
  body {
    background: var(--stage);
    position: relative;
    font-family: "Montserrat", sans-serif;
  }
  .banner {
    position: absolute;
    left: 115px;
    width: 971px;
    height: 120px;
    background: var(--banner);
    overflow: hidden;
  }
  .banner--both { top: 49px; }
  .banner--road { top: 240px; }
  .banner--mtb { top: 427px; }

  .brand {
    position: absolute;
    left: 40px; top: 10px;
    width: 100px; height: 100px;
    border: 3px solid var(--ink);
    border-radius: 50%;
    display: flex; align-items: center; justify-content: center;
    text-align: center;
  }
  .brand__name {
    font-family: "Bebas Neue", sans-serif;
    font-size: 16px;
    line-height: 1.05;
    color: var(--ink);
    letter-spacing: 0.5px;
  }

  .headline {
    position: absolute;
    font-family: "Bebas Neue", sans-serif;
    font-weight: 400;
    color: var(--white);
    line-height: 1;
    letter-spacing: 1px;
    white-space: nowrap;
  }
  .headline--dark { color: var(--ink); }

  .site-url {
    position: absolute;
    left: 176px; top: 10px;
    background: var(--white);
    color: var(--ink);
    font-family: "Montserrat", sans-serif;
    font-weight: 800;
    font-size: 16px;
    padding: 1px 6px;
    line-height: 20px;
    letter-spacing: 0.5px;
  }

  .camp-tag {
    position: absolute;
    top: 12px;
    text-align: center;
    color: var(--white);
  }
  .camp-tag__icon { display: block; margin: 0 auto 2px; }
  .camp-tag__title {
    font-family: "Bebas Neue", sans-serif;
    font-size: 26px;
    line-height: 1;
    letter-spacing: 1px;
  }
  .camp-tag__script {
    font-family: "Kaushan Script", "Brush Script MT", cursive;
    font-size: 24px;
    line-height: 1;
  }
  .divider {
    position: absolute;
    left: 740px; top: 24px;
    width: 2px; height: 72px;
    background: var(--white);
  }

  .date {
    position: absolute;
    font-weight: 800;
    font-size: 18px;
    color: var(--ink);
    letter-spacing: 0.5px;
    white-space: nowrap;
  }

  .photo {
    position: absolute;
    top: 0; height: 120px;
  }
  .photo--road {
    left: 429px; width: 280px;
    background: linear-gradient(160deg, var(--photo-road-a), var(--photo-road-b));
    -webkit-mask-image: linear-gradient(90deg, transparent 0, #000 14%, #000 86%, transparent 100%);
            mask-image: linear-gradient(90deg, transparent 0, #000 14%, #000 86%, transparent 100%);
  }
  .photo--mtb {
    left: 485px; width: 280px;
    background: linear-gradient(180deg, var(--photo-forest-a) 0%, var(--photo-forest-a) 45%, var(--photo-forest-b) 100%);
    -webkit-mask-image: linear-gradient(90deg, transparent 0, #000 8%, #000 88%, transparent 100%);
            mask-image: linear-gradient(90deg, transparent 0, #000 8%, #000 88%, transparent 100%);
  }

  .quote {
    position: absolute;
    top: 12px;
    width: 200px; height: 96px;
    color: var(--white);
    font-size: 13.5px;
    font-weight: 500;
    line-height: 1.45;
    text-align: center;
    display: flex; align-items: center; justify-content: center;
  }
  .quote__mark {
    position: absolute;
    font-family: "Montserrat", sans-serif;
    font-weight: 800;
    font-size: 22px;
    line-height: 1;
  }
  .quote__mark--open { left: 4px; top: 0; }
  .quote__mark--close { right: 4px; bottom: -6px; }
  .quote--road { left: 738px; }
  .quote--mtb { left: 758px; }
</style>
</head>
<body>

  <section class="banner banner--both" aria-label="Best cycling camps for youth">
    <div class="brand"><span class="brand__name">Quadrapedal<br>Cup</span></div>
    <span class="site-url">QUADRAPEDALCUP.ORG</span>
    <h1 class="headline" style="left:176px; top:35px; font-size:50px;">Best Cycling Camps</h1>
    <p class="headline headline--dark" style="left:176px; top:77px; font-size:36px;">For Youth</p>

    <div class="camp-tag" style="left:572px; width:120px;">
      <svg class="camp-tag__icon" width="110" height="40" viewBox="0 0 110 40" role="img" aria-label="Road and pine tree sketch">
        <rect x="0" y="0" width="110" height="40" fill="var(--banner-deep)" opacity="0.6"/>
      </svg>
      <div class="camp-tag__title">Road</div>
      <div class="camp-tag__script">Camp</div>
    </div>
    <div class="divider"></div>
    <div class="camp-tag" style="left:772px; width:150px;">
      <svg class="camp-tag__icon" width="110" height="40" viewBox="0 0 110 40" role="img" aria-label="Mountain range sketch">
        <rect x="0" y="0" width="110" height="40" fill="var(--banner-deep)" opacity="0.6"/>
      </svg>
      <div class="camp-tag__title">Mountain Bike</div>
      <div class="camp-tag__script">Camp</div>
    </div>
  </section>

  <section class="banner banner--road" aria-label="Road camps">
    <div class="brand"><span class="brand__name">Quadrapedal<br>Cup</span></div>
    <svg style="position:absolute; left:225px; top:8px;" width="70" height="26" viewBox="0 0 70 26" role="img" aria-label="Road and pine tree sketch">
      <rect x="0" y="0" width="70" height="26" fill="var(--banner-deep)" opacity="0.6"/>
    </svg>
    <h2 class="headline" style="left:168px; top:33px; font-size:61px;">Road Camps</h2>
    <p class="date" style="left:225px; top:86px;">MAY 5-7, 2017</p>
    <div class="photo photo--road" role="img" aria-label="Photo of young cyclists riding road bikes on a paved lot"></div>
    <blockquote class="quote quote--road">
      <span class="quote__mark quote__mark--open">&ldquo;</span>
      <p>Good mix of skill building<br>exercises and just riding</p>
      <span class="quote__mark quote__mark--close">&rdquo;</span>
    </blockquote>
  </section>

  <section class="banner banner--mtb" aria-label="Mountain bike camp">
    <div class="brand"><span class="brand__name">Quadrapedal<br>Cup</span></div>
    <svg style="position:absolute; left:235px; top:6px;" width="90" height="28" viewBox="0 0 90 28" role="img" aria-label="Mountain range sketch">
      <rect x="0" y="0" width="90" height="28" fill="var(--banner-deep)" opacity="0.6"/>
    </svg>
    <h2 class="headline" style="left:166px; top:40px; font-size:45px;">Mountain Bike Camp</h2>
    <p class="date" style="left:249px; top:86px;">JULY 14-16, 2017</p>
    <div class="photo photo--mtb" role="img" aria-label="Photo of a group of young riders on a road lined with pine forest"></div>
    <blockquote class="quote quote--mtb">
      <span class="quote__mark quote__mark--open">&ldquo;</span>
      <p>Well organized,<br>great coaches,<br>good location</p>
      <span class="quote__mark quote__mark--close">&rdquo;</span>
    </blockquote>
  </section>

</body>
</html>
```